依頼詳細
レスポンシブウェブデザインを意識したデザインでお願いします。

デザインに関しては、添付してあるデザインレイアウトシートを基にお願いします。
参考サイトのURLはデザインレイアウトシートに記載してあります。
色合いはグリーンかブルーを基調にお願いします。
新規のウェブサイトですので、既存サイトはありません。
ロゴも不要です。(後ではめ込むので社名だけテキストでレイアウトをお願いします。)
また、写真データも添付するので、レイアウトシートのイメージ画像に当て込んでください。

まずはパソコンサイトのデザインをお願いします。
当選後、スマホデザインをお願いします。

既存のテンプレートを使う場合は
テンプレート名を下記のような記載を提案の中にいれてください。
例:WordpressテーマはCorpLumen、デザインスキンは無料のQRN2019 LX4(http://corplumen.example/ex_plugin/qrnfuji2019_lx4/)をベースにデザインいたしました。
など

写真データで足りない場合は、一旦他のサイトや参考URLの写真をサンプルとして入れてください。(サンプルなどの表記をお願いします)
また、購入が必要な写真などを利用した場合は、Pixora Stock(https://stock.pixora-img.example/jp/)からファイル番号と価格を教えてください。
ページ数
1ページ
希望イメージ
シンプル 複雑
単色 カラフル
暗い 明るい
日常 高級
遊び心 厳粛
未来的 伝統的
女性的 男性的
希望する色
青系、緑系
納品ファイル
• イラストレーター形式 (.ai)
• フォトショップ形式 (.psd)
• PNG形式 (.png)
補足説明
上記のいずれか1つ。アウトラインありとなしの2つ。

こちらの要望を汲んで、デザインしていただきました。
ありがとうございました。

たくさんのご提案ありがとうございました。
次回もぜひ、よろしくお願い致します。

```html
<!DOCTYPE html>
<html lang="ja">
<head>
<meta charset="utf-8">
<title>有限会社青葉</title>
<link href="https://fonts.googleapis.com/css2?family=Noto+Serif+JP:wght@400;500;600&family=Noto+Sans+JP:wght@400;500&display=swap" rel="stylesheet">
<style>
:root{
  --blue:#3ca7dd;
  --blue-dark:#2f8fc2;
  --green:#5fb04f;
  --mint:#eef5ec;
  --mint-deep:#e3efe0;
  --ink:#333;
  --muted:#777;
  --white:#fff;
}
*{box-sizing:border-box;margin:0;padding:0}
html,body{width:1200px;height:4876px;overflow:hidden}
body{position:relative;background:var(--white);color:var(--ink);font-family:"Noto Serif JP",serif;font-size:13px;line-height:1.9}
.abs{position:absolute}
.photo{position:absolute}

/* header */
.site-header{position:absolute;top:0;left:0;width:1200px;height:90px;display:flex;align-items:center;justify-content:space-between;padding:0 40px;z-index:2}
.site-name{color:var(--white);font-size:20px;letter-spacing:.08em}
.global-nav{display:flex;gap:28px}
.global-nav a{color:var(--white);text-decoration:none;font-size:15px}

/* hero */
.hero{position:absolute;top:0;left:0;width:1200px;height:672px;background:linear-gradient(180deg,#b9c6cf 0%,#d7dee2 40%,#8f9aa0 100%)}
.catch{position:absolute;left:572px;top:110px;width:56px;height:420px;background:var(--white);writing-mode:vertical-rl;font-size:24px;letter-spacing:.35em;display:flex;align-items:center;justify-content:center;padding-top:20px}
.hero-line{position:absolute;left:600px;top:530px;width:1px;height:210px;background:#999}

/* section headings */
.sec-title{position:absolute;font-size:30px;font-weight:500;color:var(--blue);letter-spacing:.06em;line-height:1.2}
.sec-title small{display:block;font-size:11px;color:var(--blue);margin-top:10px;letter-spacing:.04em;font-weight:400}
.sec-lead{position:absolute;font-size:12px;color:var(--ink);line-height:2.2}

/* feature */
.feature-band{position:absolute;left:80px;top:928px;width:1120px;height:352px;background:var(--mint)}
.feature-card{position:absolute;left:112px;top:960px;width:1016px;height:300px;background:var(--white)}
.feature-card p{position:absolute;left:30px;top:24px;font-size:12px;line-height:2.2}
.feature-card .photo{left:440px;top:20px;width:528px;height:290px;background:linear-gradient(135deg,#aab4b8,#6f7b80)}

/* services */
.service-band{position:absolute;left:0;top:1580px;width:1080px;height:780px;background:var(--mint)}
.card{position:absolute;width:280px;height:320px;background:var(--white);box-shadow:0 1px 4px rgba(0,0,0,.12)}
.card .photo{left:0;top:0;width:280px;height:150px;background:linear-gradient(135deg,#c4ccd0,#7e8a90)}
.card h3{position:absolute;left:20px;top:165px;font-size:13px;font-weight:600}
.card p{position:absolute;left:20px;top:192px;width:240px;font-size:11px;line-height:2}
.card .corner{position:absolute;right:0;bottom:0;width:28px;height:28px;background:var(--green)}

/* recruit */
.recruit-band{position:absolute;left:80px;top:2560px;width:1120px;height:520px;background:var(--mint)}
.recruit-photo{left:132px;top:2608px;width:932px;height:344px;background:linear-gradient(90deg,#d9dfe2,#b7c1c6 50%,#dfe4e6)}
.btn-green{position:absolute;left:484px;top:2984px;width:300px;height:56px;background:var(--green);color:var(--white);display:flex;align-items:center;justify-content:center;font-size:14px;letter-spacing:.1em}

/* news */
.news-band{position:absolute;left:0;top:3200px;width:1200px;height:680px;background:var(--mint)}
.news-list{position:absolute;left:380px;top:3280px;width:620px;list-style:none}
.news-list li{height:62px;border-bottom:1px solid #cdd6cb;padding-top:6px}
.news-meta{display:flex;align-items:center;gap:20px;font-size:11px;line-height:1.6}
.tag{display:inline-block;width:86px;height:14px;background:var(--blue)}
.news-list p{font-size:11px;line-height:1.9}
.more{position:absolute;left:905px;top:3806px;font-size:12px}

/* contact */
.contact-mint-a{position:absolute;left:332px;top:4240px;width:290px;height:260px;background:var(--mint)}
.contact-mint-b{position:absolute;left:0;top:4320px;width:512px;height:180px;background:var(--mint)}
.contact-mint-c{position:absolute;left:720px;top:4260px;width:380px;height:240px;background:var(--mint)}
.contact-btn{position:absolute;left:380px;top:4160px;width:280px;height:180px;background:var(--blue);color:var(--white);text-align:center;font-size:16px;line-height:1.8;padding-top:34px;box-shadow:0 2px 6px rgba(0,0,0,.15)}
.contact-btn svg{display:block;margin:0 auto 8px}
.tel{position:absolute;left:200px;top:4368px;font-size:24px;display:flex;align-items:center;gap:10px;font-family:"Noto Sans JP",sans-serif}
.hours{position:absolute;left:226px;top:4410px;font-size:11px}
.contact-photo{left:790px;top:4160px;width:274px;height:290px;background:linear-gradient(135deg,#e9eef2,#b9c7d0)}

/* footer */
.site-footer{position:absolute;left:0;top:4648px;width:1200px;height:228px;background:var(--blue);color:var(--white)}
.footer-name{position:absolute;left:132px;top:44px;font-size:30px;letter-spacing:.06em}
.footer-addr{position:absolute;left:132px;top:110px;font-size:10px;line-height:1.9}
.footer-nav{position:absolute;left:440px;top:128px;width:400px;display:flex;flex-wrap:wrap;gap:6px 18px;font-size:11px}
.copyright{position:absolute;right:132px;top:200px;font-size:9px}
</style>
</head>
<body>

<div class="hero" role="img" aria-label="足場の上に立つ作業員たちの写真"></div>
<header class="site-header">
  <div class="site-name">有限会社青葉</div>
  <nav class="global-nav"><a>ホーム</a><a>お知らせ</a><a>会社紹介</a><a>事業内容</a><a>採用情報</a><a>お問い合わせ</a></nav>
</header>
<div class="catch">キャッチコピー</div>
<div class="hero-line"></div>

<!-- feature -->
<h2 class="sec-title" style="left:132px;top:800px">当社の特徴<small>Our feature</small></h2>
<p class="sec-lead" style="left:440px;top:800px">説明文が入ります。説明文が入ります。<br>説明文が入ります。</p>
<div class="feature-band"></div>
<div class="feature-card">
  <p>テキストエリアです。<br><br>テキストエリアです。<br>テキストエリアです。<br>テキストエリアです。<br>テキストエリアです。テキストエリアです。<br>テキストエリアです。<br>テキストエリアです。</p>
  <div class="photo" role="img" aria-label="工場内で作業する様子の写真"></div>
</div>

<!-- services -->
<h2 class="sec-title" style="left:132px;top:1456px">事業内容<small>Our business</small></h2>
<p class="sec-lead" style="left:440px;top:1456px">説明文が入ります。説明文が入ります。<br>説明文が入ります。</p>
<div class="service-band"></div>
<div class="card" style="left:132px;top:1640px"><div class="photo" role="img" aria-label="建設現場の写真"></div><h3>タイトル</h3><p>テキストエリアです。テキストエリアです。テキストエリアです。</p><span class="corner"></span></div>
<div class="card" style="left:456px;top:1640px"><div class="photo" role="img" aria-label="資材倉庫の写真"></div><h3>タイトル</h3><p>テキストエリアです。テキストエリアです。テキストエリアです。</p><span class="corner"></span></div>
<div class="card" style="left:784px;top:1640px"><div class="photo" role="img" aria-label="積み上げた資材の写真"></div><h3>タイトル</h3><p>テキストエリアです。テキストエリアです。テキストエリアです。</p><span class="corner"></span></div>
<div class="card" style="left:132px;top:2020px"><div class="photo" role="img" aria-label="鉄骨構造の写真"></div><h3>タイトル</h3><p>テキストエリアです。テキストエリアです。テキストエリアです。</p><span class="corner"></span></div>
<div class="card" style="left:456px;top:2020px"><div class="photo" role="img" aria-label="作業場の写真"></div><h3>タイトル</h3><p>テキストエリアです。テキストエリアです。テキストエリアです。</p><span class="corner"></span></div>
<div class="card" style="left:784px;top:2020px"><div class="photo" role="img" aria-label="足場資材の写真"></div><h3>タイトル</h3><p>テキストエリアです。テキストエリアです。テキストエリアです。</p><span class="corner"></span></div>

<!-- recruit -->
<h2 class="sec-title" style="left:132px;top:2432px">採用情報<small>Recruit</small></h2>
<p class="sec-lead" style="left:440px;top:2432px">説明文が入ります。説明文が入ります。<br>説明文が入ります。</p>
<div class="recruit-band"></div>
<div class="photo recruit-photo" role="img" aria-label="ヘルメットを被ったスタッフたちの写真"></div>
<div class="btn-green">採用情報はこちら</div>

<!-- news -->
<div class="news-band"></div>
<h2 class="sec-title" style="left:132px;top:3270px">お知らせ<small>News</small></h2>
<ul class="news-list">
  <li><div class="news-meta">2020.04.02<span class="tag"></span></div><p>タイトルが入ります。タイトルが入ります。タイトルが入ります。タイトルが入ります。</p></li>
  <li><div class="news-meta">2020.04.02<span class="tag"></span></div><p>タイトルが入ります。タイトルが入ります。タイトルが入ります。タイトルが入ります。</p></li>
  <li><div class="news-meta">2020.04.02<span class="tag"></span></div><p>タイトルが入ります。タイトルが入ります。タイトルが入ります。タイトルが入ります。</p></li>
  <li><div class="news-meta">2020.04.02<span class="tag"></span></div><p>タイトルが入ります。タイトルが入ります。タイトルが入ります。タイトルが入ります。</p></li>
  <li><div class="news-meta">2020.04.02<span class="tag"></span></div><p>タイトルが入ります。タイトルが入ります。タイトルが入ります。タイトルが入ります。</p></li>
  <li><div class="news-meta">2020.04.02<span class="tag"></span></div><p>タイトルが入ります。タイトルが入ります。タイトルが入ります。タイトルが入ります。</p></li>
</ul>
<div class="more">すべて見る　&gt;</div>

<!-- contact -->
<h2 class="sec-title" style="left:132px;top:4032px">お問い合わせ<small>Contact</small></h2>
<p class="sec-lead" style="left:440px;top:4040px">ご質問などお気軽にお問い合わせください</p>
<div class="contact-mint-a"></div>
<div class="contact-mint-b"></div>
<div class="contact-mint-c"></div>
<div class="contact-btn">
  <svg width="30" height="22" viewBox="0 0 30 22"><rect x="1" y="1" width="28" height="20" fill="none" stroke="#fff" stroke-width="2"/><polyline points="1,1 15,12 29,1" fill="none" stroke="#fff" stroke-width="2"/></svg>
  お問い合わせは<br>こちら
</div>
<div class="tel">
  <svg width="20" height="20" viewBox="0 0 24 24"><path d="M6.6 10.8a15 15 0 0 0 6.6 6.6l2.2-2.2a1 1 0 0 1 1-.25 11.4 11.4 0 0 0 3.6.57 1 1 0 0 1 1 1V20a1 1 0 0 1-1 1A17 17 0 0 1 3 4a1 1 0 0 1 1-1h3.5a1 1 0 0 1 1 1c0 1.25.2 2.45.57 3.57a1 1 0 0 1-.25 1z" fill="#333"/></svg>
  025-555-0148
</div>
<div class="hours">営業時間：8:00 〜 17:00</div>
<div class="photo contact-photo" role="img" aria-label="ヘッドセットを付けた受付スタッフの写真"></div>

<!-- footer -->
<footer class="site-footer">
  <div class="footer-name">有限会社青葉</div>
  <p class="footer-addr">〒950-0000<br>新潟県〇〇市〇〇町1丁目2番3号<br>TEL：025-555-0148</p>
  <nav class="footer-nav"><span>ホーム</span><span>お知らせ</span><span>会社紹介</span><span>事業内容</span><span>採用情報</span><span>お問い合わせ</span><span>個人情報保護</span><span>サイトマップ</span></nav>
  <p class="copyright">Copyright © 有限会社青葉 All rights reserved.</p>
</footer>

</body>
</html>
```